Postcard that needs a professional designer to create a great looking postcard

Direct mail postcard designed using the copy and graphics we have supplied. We need it to look professional, clean and eye catching.
We are marketing to builders who need to hire us to build the closets and storage in the homes they are contracted to build.

```html
<!DOCTYPE html>
<html lang="en">
<head>
<meta charset="utf-8">
<title>Harlow Closets – Builder Postcard</title>
<link rel="stylesheet" href="https://fonts.googleapis.com/css2?family=Oswald:wght@600&family=Nunito+Sans:wght@400;600&family=Italianno&display=swap">
<style>
  :root {
    --page: #eeeeee;
    --panel: #f7f7f6;
    --panel-edge: #d9d9d7;
    --shade: rgba(0,0,0,.18);
    --red: #e21c2a;
    --navy: #1d2150;
    --ink: #2b2b2b;
    --photo-a: #efe3cf;
    --photo-b: #d9c3a0;
  }
  * { box-sizing: border-box; margin: 0; padding: 0; }
  html, body { width: 1200px; height: 699px; overflow: hidden; }
  body {
    background: radial-gradient(ellipse at 50% 40%, #ffffff 0%, var(--page) 80%);
    font-family: "Nunito Sans", sans-serif;
    color: var(--ink);
    position: relative;
  }
  .shelf {
    position: absolute;
    background: linear-gradient(180deg, #ececea 0%, var(--panel) 18%, #ffffff 60%, var(--panel) 100%);
    border: 1px solid var(--panel-edge);
    box-shadow: inset 0 10px 14px -8px var(--shade), inset 10px 0 14px -10px var(--shade), 0 2px 3px rgba(0,0,0,.12);
  }
  .headline-shelf { left: 24px; top: 28px; width: 676px; height: 172px; display: flex; align-items: center; justify-content: center; }
  .headline {
    font-family: "Oswald", sans-serif;
    font-weight: 600;
    color: var(--red);
    font-size: 31px;
    line-height: 41px;
    text-align: center;
    text-shadow: 1px 1px 2px rgba(0,0,0,.18);
  }
  .needs-shelf { left: 24px; top: 220px; width: 676px; height: 240px; padding: 18px 30px 0 56px; }
  .needs { list-style: none; }
  .needs li { position: relative; font-size: 21px; line-height: 28px; margin-bottom: 15px; }
  .needs svg { position: absolute; left: -36px; top: 6px; width: 22px; height: 16px; }
  .photo-frame {
    position: absolute; left: 720px; top: 26px; width: 458px; height: 343px;
    background: linear-gradient(135deg, var(--photo-a) 0%, var(--photo-b) 100%);
    border: 1px solid var(--panel-edge);
  }
  .owners-shelf { left: 724px; top: 376px; width: 452px; height: 82px; display: flex; align-items: center; justify-content: center; }
  .owners { font-family: "Italianno", cursive; font-size: 40px; color: #222; }
  .brand-shelf { left: 24px; top: 478px; width: 382px; height: 190px; display: flex; flex-direction: column; align-items: center; justify-content: center; }
  .brand-mark { width: 22px; height: 22px; border-radius: 50%; background: var(--red); margin-bottom: 14px; }
  .brand-name { font-weight: 600; color: var(--navy); font-size: 27px; line-height: 30px; }
  .brand-sub { font-weight: 600; color: var(--navy); font-size: 18px; }
  .pitch-shelf { left: 428px; top: 476px; width: 752px; height: 192px; padding: 46px 36px 0 40px; }
  .pitch p { font-size: 16.5px; line-height: 24px; margin-bottom: 11px; }
</style>
</head>
<body>
  <section class="shelf headline-shelf">
    <h1 class="headline">It’s frustrating and time consuming<br>trying to decide how to provide<br>quality custom closets for your homeowner.</h1>
  </section>

  <section class="shelf needs-shelf">
    <ul class="needs">
      <li><svg viewBox="0 0 22 16"><path d="M2 8h16M12 2l6 6-6 6" fill="none" stroke="var(--red)" stroke-width="2.4"/></svg>You must have the same high quality in the closets that you provide in the rest of the home.</li>
      <li><svg viewBox="0 0 22 16"><path d="M2 8h16M12 2l6 6-6 6" fill="none" stroke="var(--red)" stroke-width="2.4"/></svg>You need someone that will be on time and stay within the budget.</li>
      <li><svg viewBox="0 0 22 16"><path d="M2 8h16M12 2l6 6-6 6" fill="none" stroke="var(--red)" stroke-width="2.4"/></svg>Have design options, color choices, and detailed plans to review with the homeowner.</li>
    </ul>
  </section>

  <div class="photo-frame" role="img" aria-label="Smiling homeowner standing in an organised wood-finish walk-in closet"></div>

  <section class="shelf owners-shelf">
    <p class="owners">Evan and Marcus Harlow</p>
  </section>

  <section class="shelf brand-shelf">
    <span class="brand-mark"></span>
    <p class="brand-name">Harlow Closets</p>
    <p class="brand-sub">and Storage Systems</p>
  </section>

  <section class="shelf pitch-shelf">
    <div class="pitch">
      <p>There are many contractors that are called heroes by the homeowner because of the closets Harlow Closets has provided.</p>
      <p>Naturally, you will want to call Harlow Closets to relieve your stress and frustration about having great custom closets and not just painted particle board.</p>
    </div>
  </section>
</body>
</html>
```